International Medical travel company needs professional card

We just purchased a logo through sketch nest, and now need a business card. We contract with Middle Eastern governments to bring patients who need complex medical care to the U.S. for treatment. We will upload logo. Titles, names, contact info, etc. needs to be in English on one side, Arabic on the other

Target Market(s)

Health administrators, professionals

Industry/Entity Type

Health Care

Contact Information for Business Card

logo on each side. Usual name/title/contact info

Font styles to use
Serif
Sans Serif

Colors
0255a3

Requirements
Must have
• English one side, Arabic the other

```html
<!DOCTYPE html>
<html lang="en">
<head>
<meta charset="utf-8">
<title>Meridian Care – Business Card</title>
<link rel="stylesheet" href="https://fonts.googleapis.com/css2?family=Tinos:wght@700&family=Questrial&family=Noto+Naskh+Arabic:wght@400;700&display=swap">
<style>
  :root {
    --brand-blue: #0255a3;
    --gold-dark: #a39a22;
    --gold-mid: #c9c23e;
    --gold-light: #ebe66e;
    --gold-text: #a89d2a;
    --paper: #ffffff;
    --backdrop: #2b2b2d;
    --icon: #ffffff;
  }
  * { box-sizing: border-box; margin: 0; padding: 0; }
  html, body { width: 1200px; height: 900px; overflow: hidden; }
  body { background: var(--backdrop); position: relative; font-family: "Questrial", "Century Gothic", sans-serif; }

  .card { position: absolute; width: 620px; height: 354px; overflow: hidden; }

  /* Arabic side */
  .card-arabic {
    left: 70px; top: 80px;
    background: linear-gradient(115deg, var(--gold-dark) 0%, var(--gold-mid) 30%, var(--gold-light) 55%, var(--gold-mid) 78%, var(--gold-dark) 100%);
  }
  .card-arabic .side-band { position: absolute; top: 0; bottom: 0; right: 40px; width: 44px; background: var(--brand-blue); }
  .card-arabic .brand-mark {
    position: absolute; left: 46px; top: 122px;
    display: flex; align-items: center; gap: 14px;
  }
  .card-arabic .brand-square { width: 38px; height: 38px; border: 4px solid var(--paper); }
  .card-arabic .brand-name { font-size: 34px; color: var(--paper); letter-spacing: 1px; }

  .card-arabic .details {
    position: absolute; right: 112px; top: 118px;
    direction: rtl; text-align: right; color: var(--brand-blue);
    font-family: "Noto Naskh Arabic", serif;
  }
  .card-arabic .person-name { font-size: 30px; font-weight: 700; line-height: 1.1; }
  .card-arabic .person-title { font-size: 17px; color: var(--brand-blue); margin-bottom: 12px; }
  .card-arabic .line { font-size: 15px; line-height: 1.35; }
  .card-arabic .latin { direction: ltr; font-family: "Questrial", sans-serif; font-size: 16px; line-height: 1.35; }

  /* English side */
  .card-english { left: 510px; top: 470px; background: var(--paper); }
  .card-english .side-band { position: absolute; top: 0; bottom: 0; left: 40px; width: 44px; background: var(--brand-blue); }
  .card-english .brand-mark {
    position: absolute; right: 40px; top: 48px;
    display: flex; align-items: center; gap: 12px;
  }
  .card-english .brand-square { width: 30px; height: 30px; border: 3px solid var(--gold-text); }
  .card-english .brand-name { font-size: 30px; color: var(--gold-text); letter-spacing: 1px; }

  .card-english .details { position: absolute; left: 112px; top: 168px; color: var(--brand-blue); }
  .card-english .person-name { font-family: "Tinos", "Times New Roman", serif; font-weight: 700; font-size: 24px; }
  .card-english .person-title { font-size: 17px; color: var(--gold-text); margin-bottom: 8px; }
  .card-english .line { font-size: 17px; line-height: 1.3; }

  .contact-icons {
    position: absolute; bottom: 18px; width: 44px;
    display: flex; flex-direction: column; align-items: center; gap: 7px;
  }
  .card-arabic .contact-icons { right: 40px; }
  .card-english .contact-icons { left: 40px; }
  .contact-icons svg { width: 14px; height: 14px; display: block; }
</style>
</head>
<body>

<section class="card card-arabic" lang="ar">
  <div class="brand-mark">
    <span class="brand-square"></span>
    <span class="brand-name">Meridian Care</span>
  </div>

  <div class="details">
    <p class="person-name">كريم حداد</p>
    <p class="person-title">مدير</p>
    <p class="line">طريق الميناء، 21577</p>
    <p class="line">جدة، المملكة العربية السعودية</p>
    <p class="latin">+330 5180 -4412</p>
    <p class="latin">info@meridiancare.com</p>
    <p class="latin">www.meridiancare.com</p>
  </div>

  <div class="side-band"></div>
  <div class="contact-icons">
    <svg viewBox="0 0 16 16" aria-label="Phone"><path fill="var(--icon)" d="M3.5 1.5l2.3 2.6-1.2 1.6c.9 2 2.5 3.6 4.5 4.5l1.6-1.2 2.6 2.3-1.5 2.1C6.7 13.2 2.8 9.3 1.4 3z"/></svg>
    <svg viewBox="0 0 16 16" aria-label="Email"><rect x="1.5" y="3.5" width="13" height="9" fill="none" stroke="var(--icon)" stroke-width="1.5"/><path d="M1.5 3.5L8 9l6.5-5.5" fill="none" stroke="var(--icon)" stroke-width="1.5"/></svg>
    <svg viewBox="0 0 16 16" aria-label="Website"><circle cx="8" cy="8" r="6.3" fill="none" stroke="var(--icon)" stroke-width="1.4"/><ellipse cx="8" cy="8" rx="2.8" ry="6.3" fill="none" stroke="var(--icon)" stroke-width="1.2"/><path d="M1.7 8h12.6M2.8 4.8h10.4M2.8 11.2h10.4" stroke="var(--icon)" stroke-width="1.1"/></svg>
  </div>
</section>

<section class="card card-english" lang="en">
  <div class="brand-mark">
    <span class="brand-square"></span>
    <span class="brand-name">Meridian Care</span>
  </div>

  <div class="side-band"></div>

  <div class="details">
    <p class="person-name">Karim Haddad</p>
    <p class="person-title">Director</p>
    <p class="line">Harbor Road, 21577</p>
    <p class="line">Jeddah, Saudi Arabia</p>
    <p class="line">+330 5180 -4412</p>
    <p class="line">info@meridiancare.com</p>
    <p class="line">www.meridiancare.com</p>
  </div>

  <div class="contact-icons">
    <svg viewBox="0 0 16 16" aria-label="Phone"><path fill="var(--icon)" d="M3.5 1.5l2.3 2.6-1.2 1.6c.9 2 2.5 3.6 4.5 4.5l1.6-1.2 2.6 2.3-1.5 2.1C6.7 13.2 2.8 9.3 1.4 3z"/></svg>
    <svg viewBox="0 0 16 16" aria-label="Email"><rect x="1.5" y="3.5" width="13" height="9" fill="none" stroke="var(--icon)" stroke-width="1.5"/><path d="M1.5 3.5L8 9l6.5-5.5" fill="none" stroke="var(--icon)" stroke-width="1.5"/></svg>
    <svg viewBox="0 0 16 16" aria-label="Website"><circle cx="8" cy="8" r="6.3" fill="none" stroke="var(--icon)" stroke-width="1.4"/><ellipse cx="8" cy="8" rx="2.8" ry="6.3" fill="none" stroke="var(--icon)" stroke-width="1.2"/><path d="M1.7 8h12.6M2.8 4.8h10.4M2.8 11.2h10.4" stroke="var(--icon)" stroke-width="1.1"/></svg>
  </div>
</section>

</body>
</html>
```